Pause Your Day And Browse- PYDB poster

I am the Vice President of Advocacy for the Coastline Shelfkeepers Guild. I am looking to have a set of posters made for PYDB (Pause Your Day and Browse) October 23. PYDB is a time when all school children in BC are encouraged to Pause Your Day and Browse for 15-20 minutes at some point in their day.

I would like to get a set of 2 digital posters designed (if possible it would be nice to have the option to print to both 11 x 17 and 8.5 x 11 paper). We need a poster that is high school (Grade 8-12) appropriate and one that is elementary (Grade k-7) appropriate. Both posters need to be replicated in French. All posters need to have the KWNU logo on them as well as the Coastline Shelfkeepers Guild Logo.

Here is a link to last year's successful design http://kwnu-example.org/csg/info/advocacy.html
There are two additional samples in the uploaded files section.

Each poster needs to have the following information:

-Pause Your Day and Browse (PYDB)
- The date Monday, October 23, 2017
-the logo for the KWNU (attached)
-the logo for the CSG (attached)- the logos do not have to be large.

Target Market(s)

Children ages 5-12 and 12-17 as well as their teachers

Industry/Entity Type

Teacher

Font styles to use
Sans Serif

Requirements
Must have
• Must have both logos- colours may be changed for either or both
Nice to have
• Clear, Bright lettering. Images of child or children enjoying reading
Should not have
• stereotypes

```html
<!DOCTYPE html>
<html lang="en">
<head>
<meta charset="utf-8">
<title>Pause Your Day And Browse – PYDB Poster</title>
<link rel="stylesheet" href="https://fonts.googleapis.com/css2?family=Montserrat:wght@400;700&family=Archivo+Black&display=swap">
<style>
  :root {
    --bg-centre: #f7f7f5;
    --bg-edge: #c9c9c9;
    --ink: #111111;
    --green: #1f7a2a;
    --green-deep: #0f4f19;
    --date-green: #123d1d;
    --kid-tone: #5a6f9a;
    --kid-tone-warm: #d9804a;
    --books-tone: #9a7f86;
  }
  html, body {
    margin: 0;
    padding: 0;
    overflow: hidden;
  }
  .poster {
    position: relative;
    width: 818px;
    height: 1200px;
    overflow: hidden;
    background: radial-gradient(ellipse at 50% 48%, var(--bg-centre) 0%, #ececea 55%, var(--bg-edge) 100%);
    font-family: "Montserrat", sans-serif;
  }
  .headline {
    position: absolute;
    top: 140px;
    left: 0;
    width: 100%;
    margin: 0;
    text-align: center;
    font-family: "Montserrat", sans-serif;
    font-weight: 400;
    font-size: 52px;
    line-height: 66px;
    letter-spacing: 1px;
    color: var(--ink);
    text-transform: uppercase;
  }
  .acronym {
    position: absolute;
    left: 112px;
    top: 520px;
    width: 584px;
    height: 400px;
  }
  .acronym text {
    font-family: "Archivo Black", sans-serif;
    font-size: 470px;
  }
  .art {
    position: absolute;
    border-radius: 40px;
  }
  .art--reader-left {
    left: 268px; top: 360px; width: 142px; height: 160px;
    background: linear-gradient(180deg, #3b3330 0%, var(--kid-tone) 55%, #1e2a44 100%);
  }
  .art--reader-right {
    left: 540px; top: 372px; width: 110px; height: 148px;
    background: linear-gradient(180deg, #1d1d1d 0%, #ee6a22 45%, #555555 75%, #d98a3a 100%);
  }
  .art--reader-front {
    left: 318px; top: 922px; width: 126px; height: 88px;
    border-radius: 28px;
    background: linear-gradient(180deg, var(--kid-tone-warm) 0%, #3a3535 55%, #6a4528 100%);
  }
  .art--books-left {
    left: 92px; top: 922px; width: 200px; height: 76px;
    border-radius: 6px;
    background: linear-gradient(180deg, #a89aa3 0%, #8e9d86 40%, var(--books-tone) 70%, #6f5b63 100%);
  }
  .art--books-right {
    left: 512px; top: 924px; width: 184px; height: 74px;
    border-radius: 6px;
    background: linear-gradient(180deg, #8a6b9a 0%, #a07a5b 55%, #6f5b63 100%);
  }
  .event-date {
    position: absolute;
    top: 1078px;
    left: 0;
    width: 818px;
    margin: 0;
    text-align: center;
    font-family: "Montserrat", sans-serif;
    font-weight: 700;
    font-size: 22px;
    letter-spacing: 1px;
    color: var(--date-green);
  }
  .partners {
    position: absolute;
    top: 1112px;
    left: 636px;
    display: flex;
    align-items: center;
    gap: 14px;
  }
  .partner {
    display: flex;
    align-items: center;
    gap: 5px;
    font-family: "Montserrat", sans-serif;
    font-weight: 700;
    font-size: 14px;
    color: var(--date-green);
  }
  .partner__mark {
    width: 14px;
    height: 14px;
    background: var(--date-green);
  }
  .partner__mark--round {
    border-radius: 50%;
    background: #1a3fa0;
  }
</style>
</head>
<body>
  <main class="poster">
    <h1 class="headline">Pause Your Day<br>And Browse</h1>

    <div class="art art--reader-left" role="img" aria-label="Illustration of a boy in a blue shirt sitting cross-legged on the first letter, reading a book"></div>
    <div class="art art--reader-right" role="img" aria-label="Illustration of a boy with glasses and an orange shirt sitting on the last letter, reading a book"></div>

    <svg class="acronym" viewBox="0 0 584 400" role="img" aria-label="PYDB">
      <text x="2" y="392" textLength="580" lengthAdjust="spacingAndGlyphs" fill="var(--green-deep)" transform="translate(6 4)">PYDB</text>
      <text x="2" y="392" textLength="580" lengthAdjust="spacingAndGlyphs" fill="var(--green)">PYDB</text>
    </svg>

    <div class="art art--books-left" role="img" aria-label="Illustration of stacked books in muted colours"></div>
    <div class="art art--books-right" role="img" aria-label="Illustration of two small stacks of books"></div>
    <div class="art art--reader-front" role="img" aria-label="Illustration of a red-haired child with glasses sitting on the floor, reading a green book"></div>

    <p class="event-date">MONDAY, OCTOBER 23, 2017</p>

    <div class="partners">
      <span class="partner"><span class="partner__mark"></span>CSG</span>
      <span class="partner"><span class="partner__mark partner__mark--round"></span>KWNU</span>
    </div>
  </main>
</body>
</html>
```